Tin Gull Wick Co. 3x3x3 reverse tuck product box

Coconut wax candles in paint cans. Fun, unpretentious. Every label has a different design that reflects the candle scent. Eclectic but simple branding. I want to take a minimalist approach as I need one box design to work for all of my product. Since my candles are so colorful and unique, I like Black and white (like my logo) on Kraft background. No candle names on the box, just my logo and welcome message on the back of the box with pertinent info (see "must haves"). Need to reflect my brand in one box that will work with my many unique labels. Company logo is black & white. I need to fit a particular template for printing. I really like the idea of a kraft background, but it would need to be a vector as my printing company cannot print white ink on kraft boxes. I am very open to non-kraft related art if it looks great! Please see requirement document. I have uploaded some of my product so the general feel of the brand is available. One candle per box. My website is www.tingullwick.com. My website and marketing material is minimalist since my each of my products are very unique and busy. Feel free to read my product descriptions to get a feel for my brand.

Target Market(s)

18-45 year olds

Industry/Entity Type

Candles/gifts

Font styles to use
Other font styles liked:
• NOW

Colors

Designer to choose colors to be used in the design.

Requirements
Must have
• My business logo, cruelty free logo, Paraben-free logo, recyclable , and handmade in Austin, TX
Nice to have
• I've uploaded a pic with back of box text I would like to see. My company tagline is: Coconut Wax Candle Awesomeness.
Should not have
• My candle label art on the box. I have many unique labels, and I will need this box to work for all of them.

```html
<!DOCTYPE html>
<html lang="en">
<head>
<meta charset="utf-8">
<title>Tin Gull Wick Co. – Product Box Panels</title>
<link href="https://fonts.googleapis.com/css2?family=Barlow+Semi+Condensed:wght@300;500;600&display=swap" rel="stylesheet">
<style>
  :root {
    --backdrop: #c4d9e1;
    --kraft: #d8c5a8;
    --kraft-deep: #cdb898;
    --ink: #2b2b2b;
    --band: #262626;
    --paper-light: #e6d6bd;
  }
  * { box-sizing: border-box; margin: 0; padding: 0; }
  html, body {
    width: 1200px; height: 1056px; overflow: hidden;
    background: var(--backdrop);
    font-family: "Barlow Semi Condensed", "Arial Narrow", sans-serif;
  }
  .canvas { position: relative; width: 1200px; height: 1056px; }

  .panel {
    position: absolute; width: 480px; height: 480px; overflow: hidden;
    box-shadow: 0 10px 24px rgba(40, 60, 70, .18);
  }
  .panel--kraft { background: linear-gradient(160deg, var(--kraft) 0%, var(--kraft-deep) 100%); }
  .panel--top { left: 600px; top: 40px; background: var(--band); }
  .panel--side { left: 100px; top: 536px; }
  .panel--front { left: 600px; top: 536px; }

  .brand-name {
    position: absolute; left: 0; right: 0; text-align: center;
    font-weight: 500; font-size: 34px; letter-spacing: .5px; color: var(--ink);
    display: flex; align-items: center; justify-content: center; gap: 12px;
  }
  .brand-name__mark { width: 14px; height: 14px; background: currentColor; }
  .panel--front .brand-name { top: 150px; }
  .panel--top .brand-name { top: 218px; color: var(--paper-light); font-size: 30px; }

  .base-band {
    position: absolute; left: 0; right: 0; bottom: 0; height: 86px;
    background: var(--band);
  }
  .base-rule {
    position: absolute; left: 0; right: 0; bottom: 96px; height: 3px; background: var(--ink);
  }
  .website {
    position: absolute; left: 48px; bottom: 30px;
    font-weight: 300; font-size: 17px; color: var(--paper-light); letter-spacing: .3px;
  }

  .tagline {
    position: absolute; left: 48px; bottom: 116px;
    font-weight: 600; font-size: 29px; line-height: 1.12; color: var(--ink);
  }

  .candle-art {
    position: absolute; width: 104px; height: 184px; border-radius: 8px;
    background: linear-gradient(180deg, var(--kraft-deep), #bca582);
  }
  .panel--front .candle-art { right: 40px; bottom: 96px; }
  .panel--side .candle-art { left: 64px; bottom: 96px; }

  .speech-bubble { position: absolute; left: 60px; top: 70px; }
  .speech-bubble__text {
    position: absolute; left: 0; top: 34px; width: 170px; text-align: center;
    font-weight: 500; font-size: 19px; line-height: 1.15; color: var(--paper-light);
    text-transform: uppercase; transform: rotate(12deg);
  }
</style>
</head>
<body>
<main class="canvas">

  <section class="panel panel--top" aria-label="Top flap">
    <p class="brand-name"><span class="brand-name__mark"></span>Tin Gull Wick Co.</p>
  </section>

  <section class="panel panel--kraft panel--side" aria-label="Side panel">
    <div class="speech-bubble">
      <svg width="180" height="190" viewBox="0 0 180 190">
        <path d="M14 6 H166 Q176 6 176 16 V136 Q176 146 166 146 H46 L22 178 L28 146 H14 Q4 146 4 136 V16 Q4 6 14 6 Z" fill="#262626" stroke="#2b2b2b" stroke-width="3"/>
      </svg>
      <p class="speech-bubble__text">Smelss so good<br>up in here</p>
    </div>
    <div class="candle-art" role="img" aria-label="Line drawing of a lit pillar candle"></div>
    <div class="base-rule"></div>
    <div class="base-band"></div>
  </section>

  <section class="panel panel--kraft panel--front" aria-label="Front panel">
    <p class="brand-name"><span class="brand-name__mark"></span>Tin Gull Wick Co.</p>
    <p class="tagline">Coconut Wax<br>Candle Awesomeness</p>
    <div class="candle-art" role="img" aria-label="Line drawing of a lit pillar candle"></div>
    <div class="base-rule"></div>
    <div class="base-band"><p class="website">www.tingullwick.com</p></div>
  </section>

</main>
</body>
</html>
```